Harrowmere Sack operates across the US and Australasia providing calico bags to small business through to large enterprise across all verticals. Our bags are the most premium in the market place and our customer service is second to none. Our competitive advantage lays in our competitive pricing, superior quality and outstanding customer service.

Industry/Entity Type

Business

Contact Information for Business Card

Harrowmere Sack
Delphine Marrow
Managing Director
delphine@harrowmeresack.com
www.harrowmeresack.com.au
Mobile:- 0417 689 305
Level 3, 248 Pembury Street
Melbourne Victoria Australia 3008

```html
<!DOCTYPE html>
<html lang="en">
<head>
<meta charset="utf-8">
<title>Harrowmere Sack — Business Card</title>
<link rel="stylesheet" href="https://fonts.googleapis.com/css2?family=Didact+Gothic&display=swap">
<style>
  :root {
    --backdrop: #e4e8e8;
    --card-green: #2fe38a;
    --ink-white: #ffffff;
    --card-shadow: rgba(40, 60, 60, 0.18);
  }
  * { box-sizing: border-box; margin: 0; padding: 0; }
  html, body {
    width: 1200px;
    height: 740px;
    overflow: hidden;
    background: var(--backdrop);
    font-family: "Didact Gothic", "Century Gothic", sans-serif;
    color: var(--ink-white);
  }
  .stage {
    position: relative;
    width: 1200px;
    height: 740px;
  }
  .card {
    position: absolute;
    top: 210px;
    width: 520px;
    height: 318px;
    background: var(--card-green);
    box-shadow: 0 8px 24px var(--card-shadow);
  }
  .card--front { left: 50px; }
  .card--back { left: 630px; }

  /* Front */
  .brand {
    position: absolute;
    display: flex;
    align-items: center;
    gap: 12px;
    white-space: nowrap;
  }
  .brand__name { font-weight: 400; letter-spacing: 0.5px; }
  .brand__square {
    border: 2px solid var(--ink-white);
    flex: none;
  }
  .card--front .brand {
    left: 50%;
    top: 50%;
    transform: translate(-50%, -50%);
  }
  .card--front .brand__name { font-size: 44px; }
  .card--front .brand__square { width: 34px; height: 34px; }

  /* Back */
  .card--back .brand {
    right: 26px;
    top: 26px;
    gap: 7px;
  }
  .card--back .brand__name { font-size: 19px; }
  .card--back .brand__square { width: 15px; height: 15px; border-width: 1.5px; }

  .contact-list {
    position: absolute;
    right: 26px;
    top: 74px;
    list-style: none;
    text-align: right;
  }
  .contact-list__item {
    display: flex;
    justify-content: flex-end;
    align-items: center;
    gap: 9px;
    height: 25px;
    font-size: 11px;
    letter-spacing: 0.3px;
  }
  .contact-list__tag {
    width: 15px;
    height: 15px;
    border: 1px solid var(--ink-white);
    font-size: 9px;
    line-height: 13px;
    text-align: center;
  }
  .person {
    position: absolute;
    left: 30px;
    top: 196px;
  }
  .person__name { font-size: 23px; letter-spacing: 0.4px; }
  .person__role {
    font-size: 11px;
    margin-top: 2px;
    padding-left: 62px;
    letter-spacing: 0.3px;
  }
  .address {
    position: absolute;
    left: 30px;
    right: 26px;
    bottom: 28px;
    font-size: 11px;
    text-align: right;
    letter-spacing: 0.3px;
  }
</style>
</head>
<body>
<main class="stage">
  <section class="card card--front" aria-label="Business card front">
    <div class="brand">
      <span class="brand__name">Harrowmere Sack</span>
      <span class="brand__square" aria-hidden="true"></span>
    </div>
  </section>

  <section class="card card--back" aria-label="Business card back">
    <div class="brand">
      <span class="brand__name">Harrowmere Sack</span>
      <span class="brand__square" aria-hidden="true"></span>
    </div>

    <ul class="contact-list">
      <li class="contact-list__item">0417 689 305 <span class="contact-list__tag">M</span></li>
      <li class="contact-list__item">delphine@harrowmeresack.com <span class="contact-list__tag">E</span></li>
      <li class="contact-list__item">www.harrowmeresack.com.au <span class="contact-list__tag">W</span></li>
      <li class="contact-list__item">&nbsp;<span class="contact-list__tag">A</span></li>
    </ul>

    <div class="person">
      <p class="person__name">Delphine Marrow</p>
      <p class="person__role">Managing Director</p>
    </div>

    <p class="address">Level 3, 248 Pembury Street Melbourne Victoria Australia 3008</p>
  </section>
</main>
</body>
</html>
```